New business card layout design

We need to revamp our business card layout to be more dynamic and professional. Interested in different card materials. Have a logo and color scheme. Possible something dark background light text, see what works. Will attach current card below, along with our favorite card from your website. Please test interesting ideas out with curves vs straight lines, dark background, dark/light sides, inlaid text, etc.

https://www.brivoltholdings.example/
Here is our website for theme. Let us know if you have ANY questions :)

Target Market(s)

high-net worth accredited investors and fund managers

Industry/Entity Type

Oil and Gas investment fund

Contact Information for Business Card

Name, title, number, email, website, possibly barcode to contact page on website, business name and logo

Colors
0054AA
0677BA
7BADD7
CADEEF
E8F1F8

Requirements
Must have
• Name, title, number, email, website
Nice to have
• barcode to contact page, other ideas?
Should not have
• a pink unicorn

```html
<!DOCTYPE html>
<html lang="en">
<head>
<meta charset="utf-8">
<title>Brivolt Holdings – Business Card</title>
<link rel="stylesheet" href="https://fonts.googleapis.com/css2?family=Open+Sans:wght@400;600;700&display=swap">
<style>
  :root {
    --stage: #232323;
    --card-front: #1c1c1c;
    --card-back: #19191c;
    --emboss: #2c2c31;
    --ink-light: #ffffff;
    --ink-soft: #dcdcdc;
  }
  * { box-sizing: border-box; margin: 0; padding: 0; }
  html, body {
    width: 1200px; height: 780px; overflow: hidden;
    background: var(--stage);
    font-family: "Open Sans", Arial, sans-serif;
  }
  .canvas {
    position: relative; width: 1200px; height: 780px;
    display: flex; align-items: center; justify-content: center; gap: 60px;
  }
  .card {
    position: relative; width: 525px; height: 300px;
    border-radius: 4px; overflow: hidden;
    box-shadow: 0 18px 40px rgba(0,0,0,.45);
  }
  .card--front { background: var(--card-front); }
  .card--back {
    background: var(--card-back);
    display: flex; align-items: center; justify-content: center;
  }
  .front-bands { position: absolute; inset: 0; }
  .brand-name {
    position: absolute; left: 118px; top: 46px;
    color: var(--ink-light); font-weight: 700; font-size: 28px;
    letter-spacing: 1px; line-height: 1; white-space: nowrap;
  }
  .contact-list {
    position: absolute; left: 26px; top: 118px;
    list-style: none; color: var(--ink-soft); font-size: 12px; line-height: 20px;
  }
  .contact-list li { display: flex; align-items: center; gap: 7px; white-space: nowrap; }
  .contact-icon { width: 11px; height: 11px; fill: var(--ink-soft); flex: none; }
  .holder {
    position: absolute; right: 38px; top: 178px; text-align: right;
    color: var(--ink-light);
  }
  .holder-name { font-weight: 700; font-size: 28px; line-height: 1.1; white-space: nowrap; }
  .holder-title, .holder-company { font-size: 14px; line-height: 1.3; }
  .back-name {
    color: var(--emboss); font-weight: 700; font-size: 44px; letter-spacing: 2px;
  }
</style>
</head>
<body>
<main class="canvas">
  <section class="card card--front" aria-label="Card front">
    <svg class="front-bands" viewBox="0 0 525 300" aria-hidden="true">
      <polygon points="0,268 244,268 258,279 258,284 240,272 0,272" fill="#ffffff"/>
      <polygon points="252,280 500,280 500,168 525,168 525,300 270,300 270,292 262,287" fill="#ffffff"/>
      <rect x="0" y="291" width="262" height="3" fill="#ffffff"/>
    </svg>
    <div class="brand-name">BRIVOLT HOLDINGS</div>
    <ul class="contact-list">
      <li><svg class="contact-icon" viewBox="0 0 24 24"><path d="M6.6 10.8a15 15 0 0 0 6.6 6.6l2.2-2.2c.3-.3.7-.4 1-.2 1.1.4 2.3.6 3.6.6.6 0 1 .4 1 1V20c0 .6-.4 1-1 1A17 17 0 0 1 3 4c0-.6.4-1 1-1h3.5c.6 0 1 .4 1 1 0 1.3.2 2.5.6 3.6.1.3 0 .7-.2 1z"/></svg>(555) 014-2290</li>
      <li><svg class="contact-icon" viewBox="0 0 24 24"><path d="M12 2a10 10 0 1 0 0 20 10 10 0 0 0 0-20zm6.9 6h-3a15 15 0 0 0-1.3-3.9A8 8 0 0 1 18.9 8zM12 4c.8 1.2 1.5 2.5 1.9 4h-3.8c.4-1.5 1.1-2.8 1.9-4zM4.3 14a8 8 0 0 1 0-4h3.4a16 16 0 0 0 0 4zm.8 2h3a15 15 0 0 0 1.3 3.9A8 8 0 0 1 5.1 16zm3-8h-3a8 8 0 0 1 4.3-3.9C8.8 5.3 8.4 6.6 8.1 8zM12 20c-.8-1.2-1.5-2.5-1.9-4h3.8c-.4 1.5-1.1 2.8-1.9 4zm2.3-6H9.7a14 14 0 0 1 0-4h4.6a14 14 0 0 1 0 4zm.3 5.9c.6-1.2 1-2.5 1.3-3.9h3a8 8 0 0 1-4.3 3.9zm1.7-5.9a16 16 0 0 0 0-4h3.4a8 8 0 0 1 0 4z"/></svg>www.brivoltholdings.example</li>
      <li><svg class="contact-icon" viewBox="0 0 24 24"><path d="M2 5h20v14H2zm2 2v.5l8 5 8-5V7zm0 2.8V17h16V9.8l-8 5z"/></svg>daniel.reyes@brivoltholdings.example</li>
    </ul>
    <div class="holder">
      <p class="holder-name">Daniel Reyes</p>
      <p class="holder-title">CEO</p>
      <p class="holder-company">Brivolt Holdings</p>
    </div>
  </section>
  <section class="card card--back" aria-label="Card back">
    <p class="back-name">BRIVOLT HOLDINGS</p>
  </section>
</main>
</body>
</html>
```